Utility Contractor looking for a new website

Water and wastewater utility contractor looking to create a new website that highlights our various services. We are looking for modern web presence that can be updated with current projects and new services as we grow. We have an existing logo that we would like to incorporate into the overall design of the site
Updates

Hi, Thank you for all the design submissions. I have had some time to review and have eliminated the ones I feel are not what I am looking for. Based on the designs that remain, I am looking for a clean (not to many bold colours), modern look that is not to busy (long scrolling page), Thanks, Dean

Target Market(s)

project managers, strata boards, owners, people who make decisions as to who operates their water/wastewater system

Industry/Entity Type

Utility

Font styles to use
Sans Serif

Requirements
Must have
• A min page that describes the company and what we do, A page for each of our services that outlines the service and the benefits of it. the look must be consistent throughout. additionally each service page should have some images related to the service

```html
<!DOCTYPE html>
<html lang="en">
<head>
<meta charset="utf-8">
<title>Valley Flowline Ltd. – Contact Us</title>
<link href="https://fonts.googleapis.com/css2?family=Open+Sans:wght@400;700;800&family=Pontano+Sans&display=swap" rel="stylesheet">
<style>
  :root {
    --page-bg: #e8e8e8;
    --frame-bg: #eeeeee;
    --frame-line: #d6d6d6;
    --panel: #ffffff;
    --navy: #0f2d4f;
    --blue: #2469ad;
    --button: #3a7fc1;
    --green: #1c9e5a;
    --ink: #1a1a1a;
    --text: #555555;
    --field: #f2f2f2;
    --field-line: #d2d2d2;
    --water-top: #cfd8df;
    --water-mid: #7fa5c4;
    --water-low: #e9ecef;
  }
  * { box-sizing: border-box; margin: 0; padding: 0; }
  html, body { width: 1200px; height: 770px; overflow: hidden; }
  body {
    position: relative;
    background: var(--page-bg);
    font-family: "Pontano Sans", "Open Sans", sans-serif;
    color: var(--text);
  }
  .brand {
    position: absolute; left: 120px; top: 24px;
    font-family: "Open Sans", sans-serif; font-weight: 800;
    color: var(--navy); font-size: 39px; line-height: 37px; letter-spacing: -1px;
  }
  .call-now {
    position: absolute; right: 118px; top: 58px;
    font-family: "Open Sans", sans-serif; font-size: 29px; color: var(--ink);
  }
  .call-now .number { color: var(--green); font-size: 34px; }
  .nav-frame {
    position: absolute; left: 118px; top: 122px; width: 964px; height: 49px;
    background: var(--frame-bg); border: 1px solid var(--frame-line);
  }
  .nav {
    position: absolute; left: 8px; top: 7px; width: 946px; height: 34px;
    background: var(--panel); list-style: none;
  }
  .nav li { position: absolute; top: 8px; font-size: 15px; color: var(--text); }
  .nav li.active { color: var(--blue); }
  .main-frame {
    position: absolute; left: 118px; top: 185px; width: 964px; height: 500px;
    background: var(--frame-bg); border: 1px solid var(--frame-line);
  }
  .main {
    position: absolute; left: 9px; top: 10px; width: 944px; height: 480px;
    background: var(--panel);
  }
  h2 {
    position: absolute; font-weight: 400; font-size: 29px; color: var(--blue);
  }
  .address {
    position: absolute; left: 22px; top: 68px; width: 310px;
    font-size: 17.5px; line-height: 23px;
  }
  .divider {
    position: absolute; left: 22px; top: 126px; width: 297px;
    border-top: 1px dotted #9a9a9a;
  }
  .phones { position: absolute; left: 21px; top: 148px; list-style: none; }
  .phones li { height: 30px; font-size: 17.5px; display: flex; align-items: center; gap: 3px; }
  .phones svg { width: 21px; height: 14px; }
  .map {
    position: absolute; left: 20px; top: 244px; width: 380px; height: 213px;
    background: linear-gradient(135deg, #ece9e2 0%, #e3e0d8 55%, #dfe6d6 100%);
    border: 1px solid #cfcfcf;
  }
  .field {
    position: absolute; background: var(--field); border: 1px solid var(--field-line);
    font-size: 16px; color: #444; padding: 10px 8px;
  }
  .submit {
    position: absolute; left: 437px; top: 402px; width: 143px; height: 55px;
    background: var(--button); padding: 4px;
  }
  .submit span {
    display: flex; align-items: center; justify-content: center;
    width: 100%; height: 100%; border: 1.5px solid #fff;
    color: #fff; font-size: 24px;
  }
  .water {
    position: absolute; left: 0; top: 688px; width: 1200px; height: 82px;
    background: linear-gradient(180deg, var(--water-top) 0%, var(--water-mid) 22%, #c7d6e2 45%, var(--water-low) 75%);
  }
</style>
</head>
<body>
  <header>
    <div class="brand">VALLEY<br>FLOWLINE LTD.</div>
    <div class="call-now">Call Now: <span class="number">250 555-0142</span></div>
  </header>

  <nav class="nav-frame">
    <ul class="nav">
      <li style="left:57px">Home</li>
      <li style="left:186px">About Us</li>
      <li style="left:339px">Our Services</li>
      <li style="left:513px">Testimonials</li>
      <li style="left:687px">News</li>
      <li class="active" style="left:815px">Contact Us</li>
    </ul>
  </nav>

  <main class="main-frame">
    <div class="main">
      <section class="reach">
        <h2 style="left:21px; top:22px">Reach Us</h2>
        <p class="address">Valley Flowline Ltd. 1180 Cedarbend Road Lakeview, BC - V0X 2K4</p>
        <div class="divider"></div>
        <ul class="phones">
          <li><svg viewBox="0 0 21 14"><path fill="#2469ad" d="M1 5 C4 0 17 0 20 5 L17 7 L14 5 L14 3 C12 2 9 2 7 3 L7 5 L4 7 Z M5 8 L16 8 L18 13 L3 13 Z"/><circle cx="10.5" cy="10.3" r="1.8" fill="#fff"/></svg>(+1) 250 555-0142</li>
          <li><svg viewBox="0 0 21 14"><path fill="#2469ad" d="M1 5 C4 0 17 0 20 5 L17 7 L14 5 L14 3 C12 2 9 2 7 3 L7 5 L4 7 Z M5 8 L16 8 L18 13 L3 13 Z"/><circle cx="10.5" cy="10.3" r="1.8" fill="#fff"/></svg>(+1) 888 555-0199</li>
          <li><svg viewBox="0 0 21 14"><path fill="#2469ad" d="M1 5 C4 0 17 0 20 5 L17 7 L14 5 L14 3 C12 2 9 2 7 3 L7 5 L4 7 Z M5 8 L16 8 L18 13 L3 13 Z"/><circle cx="10.5" cy="10.3" r="1.8" fill="#fff"/></svg>(+1) 250 555-0173</li>
        </ul>
        <div class="map" role="img" aria-label="Street map showing the office location"></div>
      </section>

      <section class="contact-form">
        <h2 style="left:435px; top:22px">Contact Us</h2>
        <div class="field" style="left:437px; top:62px; width:489px; height:41px">Name</div>
        <div class="field" style="left:437px; top:112px; width:231px; height:41px">Email</div>
        <div class="field" style="left:695px; top:112px; width:231px; height:41px">Phone</div>
        <div class="field" style="left:437px; top:162px; width:489px; height:73px">Address</div>
        <div class="field" style="left:437px; top:245px; width:489px; height:148px">Message</div>
        <div class="submit"><span>SUBMIT</span></div>
      </section>
    </div>
  </main>

  <div class="water" role="img" aria-label="Decorative band of rippling water with bubbles"></div>
</body>
</html>
```